依頼詳細
・シュリンクラベルのデザインをお願いします。500g入チューブボトルに被せます。(展開図添付②)
・弊社ロゴ、商品名等を入れた表面のデザインと、裏面のベースデザインをお願い致します。
・表面デザインについては、以下の点を考慮してください。
①カテゴリーテーマである「和風」「高級」をイメージしたものを希望します。その上で「みのれ」らしさを付加してください。
②和風柄やイラストを使用いただいても構いませんが、メニューなどの写真の使用は希望していません。
③基本的に自由にデザインして頂きたいのですが、本商品のデザインをベースに今後”和風系”カテゴリーとして「黒蜜」「抹茶」もリニューアルしていきますので、そのことを意識しながら提案してください。
④既存“フルーツ系”“スイーツ系””オリジナルソース・ゼリー系”カテゴリーのデザインとは、はっきり区別できるデザインを希望します。
⑤業務用の商品ですが、シンプルすぎない、洗練されたデザインを希望します。
記載項目
・キャップの色は赤、黄、オレンジ、緑、明るいオリーブ、青、こげ茶色のいずれかを選択できますが、希望色があれば別途ご指定ください。(新たに作ります)
【メインデザイン面に表記する文言】
・商品名① 『 みのれ 』 : 最も目立つ大きさで入れてください。
・商品名② 『 MINORE Sauce 』 : 商品名①より小さい文字で入れてください。
・『500g』(8ポイント以上の文字で)
・ 『桜花・桜葉入り』や『桜の花びら・葉入り』というような文言を入れてください。(8ポイント以上の文字で)
・『TK FOOD CO,LTD.』:位置とサイズは弊社既存品(資料添付④⑤)に合わせて下方の位置にお願いします。
色の指定はありません。
・TKロゴ(添付データのいずれか1つを使用):位置とサイズは弊社既存品(資料添付④⑤)に合わせて上方中央の位置にお願いします。“BRAND”は消して使用してください。色の指定はありません。
※裏面には以下の情報を組み込みます。
一括表示、使用上の注意、JANコード、お問い合わせ先、キャップの開け方、リサイクルマーク等
※ご提案のデータはPDFかjpgでお願いします。
希望イメージ
シンプル 複雑
単色 カラフル
暗い 明るい
日常 高級
遊び心 厳粛
未来的 伝統的
女性的 男性的
希望する色
赤系、金色などのメタリックカラー
納品ファイル
• イラストレーター形式 (.ai)
補足説明
・裏面デザインについては、表面のデザインを踏襲したものでも、全く別のデザインでも構いませんが、ほぼ全面に表示などの文字情報が入ります(一括表示枠内などは無地になります)ので、その点を考慮してご提案ください。(資料添付③)
「みのれ」商品として来春を販売のピークにしたく締め切りを急ぎましたが、未だご提案いただけない状況で、開発計画日程ギリギリのラインで締め切りを延期させていただきます。
同時に依頼金額もアップいたしましたので、モアラーの皆様ハリキッてご提案ください。
よろしくお願い致します。

まずは鮮やかなピンクに惹かれました。
また、シンプルな中にも沢山のデザインが施されていて、かつ全体は上品にまとまっている事が決め手となりました。

このたびは沢山のご提案をいただき、有難うございました。
どのデザインも個性的で、またこちらの要望をよく配慮いただいていたと感じました。社内で大変悩んだ末、やっとの事で一つに絞らせて頂きました。
次回もモアラーズにてお願いさせて頂く予定ですので、今回ご当選されなかったデザイナー様も是非ご提案いただきたいと思います。
有難うございました。

```html
<!DOCTYPE html>
<html lang="ja">
<head>
<meta charset="utf-8">
<title>みのれ MINORE Sauce 500g シュリンクラベル</title>
<link rel="stylesheet" href="https://fonts.googleapis.com/css2?family=Shippori+Mincho:wght@500;700&family=Noto+Serif+JP:wght@500&display=swap">
<style>
  :root {
    --canvas: #ffffff;
    --film: #d6d6d8;
    --film-inner: #e4e4e6;
    --cap-red: #e0234e;
    --body-pink: #db2450;
    --paper: #efe6d2;
    --paper-edge: #e2d6bb;
    --ink: #2b2520;
    --band: #1a1a1a;
    --gold-light: #f3dd97;
    --gold: #d2a94a;
    --gold-dark: #a97e2a;
    --perforation: #ffffff;
  }
  html, body {
    margin: 0;
    padding: 0;
    width: 1200px;
    height: 2392px;
    overflow: hidden;
    background: var(--canvas);
  }
  .label {
    position: relative;
    width: 1200px;
    height: 2392px;
    font-family: "Shippori Mincho", "Noto Serif JP", serif;
  }
  .dieline {
    position: absolute;
    inset: 0;
  }
  .brand-mark {
    position: absolute;
    left: 0;
    width: 1200px;
    top: 715px;
    text-align: center;
    font-size: 64px;
    font-weight: 700;
    letter-spacing: 6px;
    color: var(--cap-red);
    line-height: 1;
  }
  .product-name {
    position: absolute;
    left: 520px;
    top: 860px;
    width: 180px;
    writing-mode: vertical-rl;
    font-size: 168px;
    font-weight: 500;
    letter-spacing: 18px;
    color: var(--ink);
    line-height: 1;
  }
  .product-sub {
    position: absolute;
    left: 416px;
    top: 950px;
    writing-mode: vertical-rl;
    font-family: "Noto Serif JP", serif;
    font-size: 26px;
    letter-spacing: 9px;
    color: var(--ink);
    line-height: 1;
  }
  .contents-badge {
    position: absolute;
    left: 728px;
    top: 1536px;
    width: 184px;
    height: 184px;
    border-radius: 50%;
    background: radial-gradient(circle at 35% 30%, var(--gold-light), var(--gold) 55%, var(--gold-dark));
    display: flex;
    flex-direction: row-reverse;
    justify-content: center;
    align-items: flex-start;
    gap: 6px;
    padding-top: 34px;
    box-sizing: border-box;
  }
  .contents-badge span {
    writing-mode: vertical-rl;
    font-size: 38px;
    font-weight: 700;
    color: var(--ink);
    line-height: 1;
  }
  .contents-badge .small {
    font-size: 28px;
    margin-top: 36px;
  }
  .net-weight {
    position: absolute;
    left: 0;
    width: 1200px;
    top: 1690px;
    text-align: center;
    font-family: "Noto Serif JP", serif;
    font-size: 68px;
    letter-spacing: 4px;
    color: var(--ink);
    line-height: 1;
  }
  .open-tab {
    position: absolute;
    left: 560px;
    top: 455px;
    font-family: "Noto Serif JP", serif;
    font-size: 14px;
    letter-spacing: 2px;
    color: #9a9a9c;
  }
</style>
</head>
<body>
<main class="label">
  <svg class="dieline" width="1200" height="2392" viewBox="0 0 1200 2392" xmlns="http://www.w3.org/2000/svg">
    <defs>
      <linearGradient id="blossom-tone" x1="0" y1="0" x2="0" y2="1">
        <stop offset="0" stop-color="#db2450"/>
        <stop offset="1" stop-color="#cf1f48"/>
      </linearGradient>
    </defs>
    <!-- cap -->
    <rect class="cap" x="512" y="8" width="176" height="88" fill="var(--cap-red)"/>
    <!-- shrink film outline -->
    <path class="film" d="M440 112 H760 V300 C760 360 800 380 880 390 L1160 400 V2340 H40 V400 L320 390 C400 380 440 360 440 300 Z" fill="var(--film)"/>
    <path class="film-inner" d="M470 140 H730 V300 C730 380 790 410 880 420 L1112 430 V2312 H88 V430 L320 420 C410 410 470 380 470 300 Z" fill="var(--film-inner)"/>
    <!-- perforation -->
    <line class="perforation" x1="88" y1="472" x2="1112" y2="472" stroke="var(--perforation)" stroke-width="4" stroke-dasharray="14 10"/>
    <path class="open-arrow" d="M520 462 L545 462 L545 455 L558 466 L545 477 L545 470 L520 470 Z" fill="#9a9a9c"/>
    <!-- main body -->
    <rect class="body-panel" x="88" y="632" width="1024" height="1680" fill="var(--body-pink)"/>
    <!-- blossom pattern area -->
    <rect role="img" aria-label="金色の桜の花の和柄模様" x="88" y="1880" width="1024" height="432" fill="url(#blossom-tone)"/>
    <!-- paper strip -->
    <path class="paper-strip" d="M340 600 L372 592 L410 604 L452 594 L500 606 L548 596 L600 604 L652 594 L700 606 L748 596 L800 604 L838 594 L860 602 L856 700 L864 820 L854 980 L862 1140 L852 1300 L862 1460 L854 1620 L860 1810 H340 L346 1620 L336 1460 L346 1300 L338 1140 L346 980 L336 820 L344 700 Z" fill="var(--paper)" stroke="var(--paper-edge)" stroke-width="2"/>
    <rect class="band" x="328" y="1808" width="536" height="24" fill="var(--band)"/>
  </svg>

  <span class="open-tab">OPEN</span>
  <div class="brand-mark">TK</div>
  <h1 class="product-name" style="margin:0">みのれ</h1>
  <p class="product-sub" style="margin:0">MINORE SAUCE</p>
  <div class="contents-badge">
    <span>桜花</span>
    <span>桜葉</span>
    <span class="small">入り</span>
  </div>
  <p class="net-weight" style="margin:0">500g</p>
</main>
</body>
</html>
```